Label for Wines Design

I need a label design for a start-up business that makes grape wines. The label of wine features a picture frame on the edges of the wine bottle label. So each style of wine (red, white, sparkling, rose etc) will feature a different colour. As you can picture there is already a lot going on in this label.

My trademark is 'tamo', means 'Virgin pure love',type of wines: Sauvignon Blanc, Merlot, Pino noir etc. All in Caps, a Juxtaposition of old & modern. Bold & thick letters to grab attention on the wine store shelves. Maybe letter spacing squeezed together as the wine label is only 4inches wide...the text 'tamo' must fit on one line! No Cursive or curvy lines! Colors open to black, green, yellow, purple must be natural colors hues in nature.

New Zealand wines are New worlds wines,green and astringency,unique fruity, just as virgin pure love, is an infatuation, lovesickness, never forget......

Target Market(s)

New Zealand and Asian
food & wine lovers all ages

Industry/Entity Type

Business

Font styles to use
Decorative
Script

Colors

Designer to choose colors to be used in the design.

Requirements
Must have
• Front Label and back label
Nice to have
• Wines-feeling is green and astringency,unique fruity, just as virgin pure love, is an infatuation, lovesickness, never forget......

```html
<!DOCTYPE html>
<html lang="en">
<head>
<meta charset="utf-8">
<title>Tamo Sauvignon Blanc – Front Label</title>
<link rel="stylesheet" href="https://fonts.googleapis.com/css2?family=Libre+Baskerville&family=Lato:wght@400&display=swap">
<style>
  :root {
    --canvas-bg: #f4f4f2;
    --label-white: #f7f7f7;
    --label-grey: #e6e6e8;
    --ink: #333336;
    --ink-soft: #4a4a4e;
    --sky-top: #d8d2c8;
    --sky-low: #eeeae4;
    --hill: #b9b2a6;
    --vine-green: #6f8a45;
    --vine-light: #8fa85c;
    --vine-shadow: #4a3f5c;
  }
  * { margin: 0; padding: 0; box-sizing: border-box; }
  html, body {
    width: 939px;
    height: 1200px;
    overflow: hidden;
    background: var(--canvas-bg);
  }
  .label {
    position: absolute;
    left: 60px;
    top: 175px;
    width: 820px;
    height: 850px;
    background: var(--label-white);
    box-shadow: 0 2px 10px rgba(0,0,0,0.12);
    overflow: hidden;
  }
  .label__masthead {
    height: 300px;
    display: flex;
    align-items: center;
    padding: 0 40px;
    background: linear-gradient(90deg, var(--label-grey), var(--label-white) 55%, var(--label-grey));
  }
  .brand-name {
    font-family: "Libre Baskerville", serif;
    font-weight: 400;
    font-size: 190px;
    line-height: 1;
    color: var(--ink);
  }
  .label__scene {
    height: 390px;
    background:
      linear-gradient(180deg,
        var(--sky-top) 0%,
        var(--sky-low) 30%,
        var(--hill) 44%,
        var(--vine-green) 52%,
        var(--vine-shadow) 64%,
        var(--vine-green) 74%,
        var(--vine-light) 86%,
        var(--vine-shadow) 100%);
  }
  .label__footer {
    height: 160px;
    display: flex;
    align-items: center;
    justify-content: space-between;
    padding: 0 70px 0 26px;
    background: var(--label-white);
  }
  .varietal {
    font-family: "Libre Baskerville", serif;
    font-size: 34px;
    color: var(--ink);
    line-height: 1.2;
  }
  .origin {
    font-family: "Lato", sans-serif;
    font-size: 15px;
    letter-spacing: 2.5px;
    color: var(--ink-soft);
    margin-top: 14px;
  }
  .vintage {
    font-family: "Libre Baskerville", serif;
    font-size: 50px;
    color: var(--ink);
    margin-top: 24px;
  }
</style>
</head>
<body>
  <div class="label">
    <header class="label__masthead">
      <p class="brand-name">TAMO</p>
    </header>
    <div class="label__scene" role="img" aria-label="Photograph of a vineyard at sunrise with rows of vines, a lone tree and misty hills"></div>
    <footer class="label__footer">
      <div class="label__variety">
        <p class="varietal">Sauvignon Blanc</p>
        <p class="origin">NEW ZEALAND WINE</p>
      </div>
      <p class="vintage">2017</p>
    </footer>
  </div>
</body>
</html>
```